brivox new business card design project

we need a new business card design. you can view info about us @ brivox.com. i have attached an example of our previous card with our previous name that we no longer use. We really liked the design, colors etc. look below to see more info about this project. it asks for a limited number of words. please see our website for more info about our compnay.

Target Market(s)

law enforcement

Contact Information for Business Card

i have uploaded an example of what we used before that we liked.

Font styles to use
Serif

```html
<!DOCTYPE html>
<html lang="en">
<head>
<meta charset="utf-8">
<title>brivox business card</title>
<link href="https://fonts.googleapis.com/css2?family=Arimo:wght@700&family=Montserrat:wght@300;400;600&display=swap" rel="stylesheet">
<style>
  :root {
    --backdrop: #1e1f21;
    --card: #0f1c26;
    --card-edge: #0b151d;
    --ink: #ffffff;
    --soft-ink: #e6edf2;
    --accent: #2e7fd0;
    --glow: #4fa8e6;
    --rule: #8a969e;
  }
  html, body {
    margin: 0;
    width: 1200px;
    height: 1200px;
    overflow: hidden;
    background: var(--backdrop);
  }
  .canvas {
    position: relative;
    width: 1200px;
    height: 1200px;
  }
  .card {
    position: absolute;
    left: 150px;
    width: 900px;
    height: 514px;
    border-radius: 26px;
    background: linear-gradient(160deg, #13232f 0%, var(--card) 55%, var(--card-edge) 100%);
    overflow: hidden;
    box-shadow: 0 18px 40px rgba(0,0,0,0.55);
  }
  .card--front { top: 56px; }
  .card--back { top: 630px; }

  /* Front */
  .network-map {
    position: absolute;
    left: 110px;
    top: 30px;
    width: 700px;
    height: 440px;
    border-radius: 42% 48% 40% 46% / 38% 40% 58% 52%;
    background:
      radial-gradient(circle at 55% 72%, rgba(79,168,230,0.75) 0%, rgba(79,168,230,0) 22%),
      radial-gradient(ellipse at 50% 50%, rgba(46,127,208,0.45) 0%, rgba(30,80,130,0.25) 55%, rgba(15,28,38,0) 78%);
  }
  .headline {
    position: absolute;
    left: 0;
    right: 0;
    top: 150px;
    text-align: center;
    font-family: "Arimo", Arial, sans-serif;
    font-weight: 700;
    color: var(--ink);
    font-size: 54px;
    line-height: 1.08;
    letter-spacing: 1px;
    margin: 0;
    text-shadow: 0 2px 8px rgba(0,0,0,0.4);
  }
  .tagline {
    position: absolute;
    left: 0;
    right: 0;
    top: 282px;
    text-align: center;
    font-family: "Arimo", Arial, sans-serif;
    font-weight: 700;
    color: var(--soft-ink);
    font-size: 19px;
    margin: 0;
  }

  /* Back */
  .brand {
    position: absolute;
    left: 90px;
    top: 200px;
    font-family: "Montserrat", sans-serif;
    font-weight: 300;
    font-size: 68px;
    letter-spacing: 10px;
    color: var(--ink);
    margin: 0;
  }
  .divider {
    position: absolute;
    left: 460px;
    top: 150px;
    width: 1px;
    height: 210px;
    background: var(--rule);
  }
  .contact {
    position: absolute;
    left: 500px;
    top: 150px;
    font-family: "Montserrat", sans-serif;
    color: var(--ink);
  }
  .contact__name {
    margin: 0;
    font-weight: 600;
    font-size: 28px;
  }
  .contact__role {
    margin: 2px 0 22px;
    font-weight: 400;
    font-size: 21px;
    color: var(--accent);
  }
  .contact__address {
    margin: 0 0 20px;
    font-style: normal;
    font-size: 21px;
    line-height: 1.3;
  }
  .contact__list {
    list-style: none;
    margin: 0;
    padding: 0;
    font-size: 21px;
  }
  .contact__list li {
    display: flex;
    align-items: center;
    gap: 14px;
    line-height: 1.45;
  }
  .contact__list svg {
    width: 20px;
    height: 20px;
    fill: none;
    stroke: var(--accent);
    stroke-width: 2;
  }
  .base-band {
    position: absolute;
    left: 0;
    right: 0;
    bottom: 0;
    height: 34px;
    background: var(--accent);
  }
  .base-band::before {
    content: "";
    position: absolute;
    left: 0;
    right: 0;
    top: -10px;
    height: 4px;
    background: var(--accent);
  }
</style>
</head>
<body>
<main class="canvas">
  <section class="card card--front">
    <div class="network-map" role="img" aria-label="Glowing network map of the United States with connected nodes"></div>
    <h1 class="headline">LAW ENFORCEMENT<br>INNOVATION</h1>
    <p class="tagline">Automating Processes and Connecting Jurisdictions</p>
  </section>

  <section class="card card--back">
    <p class="brand">BRIVOX</p>
    <div class="divider"></div>
    <div class="contact">
      <p class="contact__name">Marcus Ellery</p>
      <p class="contact__role">CEO/Founder</p>
      <address class="contact__address">4215 Linden Park Road<br>Austin, TX 78745</address>
      <ul class="contact__list">
        <li>
          <svg viewBox="0 0 24 24" aria-hidden="true"><path d="M5 3h4l2 5-3 2a12 12 0 0 0 6 6l2-3 5 2v4a2 2 0 0 1-2 2A17 17 0 0 1 3 5a2 2 0 0 1 2-2z"/></svg>
          866.555.0142
        </li>
        <li>
          <svg viewBox="0 0 24 24" aria-hidden="true"><rect x="3" y="5" width="18" height="14" rx="1"/><path d="M3 6l9 7 9-7"/></svg>
          info@brivox.com
        </li>
        <li>
          <svg viewBox="0 0 24 24" aria-hidden="true"><circle cx="12" cy="12" r="9"/><path d="M3 12h18M12 3c3 3 3 15 0 18M12 3c-3 3-3 15 0 18"/></svg>
          brivox.com
        </li>
      </ul>
    </div>
    <div class="base-band"></div>
  </section>
</main>
</body>
</html>
```